Kestrel Roadway Wheels

I need a wrap designed for a box truck. The company is a mobile tire shop. It’s a tire shop on wheels, that comes anywhere you are to service your tires.

```html
<!DOCTYPE html>
<html lang="en">
<head>
<meta charset="utf-8">
<title>Kestrel Roadway Wheels – Box Truck Wrap</title>
<link href="https://fonts.googleapis.com/css2?family=Bebas+Neue&family=Oswald:wght@500;600&display=swap" rel="stylesheet">
<style>
  :root {
    --brand-blue: #1f6f9c;
    --brand-blue-dark: #175a80;
    --ink: #1d1f22;
    --panel-white: #ffffff;
    --panel-grey: #eef0f2;
    --canvas: #e4e6e9;
    --tire-dark: #2a2c2f;
    --tire-mid: #5c6066;
    --worker-red: #d8322a;
    --worker-grey: #6d737b;
  }
  * { box-sizing: border-box; margin: 0; padding: 0; }
  html, body { width: 1200px; height: 900px; overflow: hidden; }
  body { background: var(--canvas); font-family: "Bebas Neue", "Oswald", sans-serif; color: var(--ink); position: relative; }

  .box-side {
    position: absolute; left: 40px; top: 40px; width: 1120px; height: 560px;
    background: linear-gradient(180deg, var(--panel-white), var(--panel-grey));
    overflow: hidden; box-shadow: 0 2px 10px rgba(0,0,0,.15);
  }
  .box-side__band { position: absolute; inset: 0; width: 1120px; height: 560px; }
  .box-side__headline {
    position: absolute; left: 90px; top: 36px; color: #fff;
    font-size: 84px; line-height: 0.95; letter-spacing: 0.5px;
  }
  .worker-photo {
    position: absolute; left: 870px; top: 20px; width: 210px; height: 530px;
    background: linear-gradient(180deg, var(--worker-red) 0%, var(--worker-red) 22%, var(--worker-grey) 23%, var(--worker-grey) 80%, var(--tire-dark) 100%);
    border-radius: 6px; opacity: .92;
  }
  .service-list {
    position: absolute; left: 380px; top: 222px; list-style: none;
    font-size: 27px; line-height: 29px;
  }
  .service-list li::before {
    content: ""; display: inline-block; width: 9px; height: 9px; border-radius: 50%;
    background: var(--brand-blue); margin-right: 14px; vertical-align: 5px;
  }
  .tire-row {
    position: absolute; left: 30px; top: 400px; width: 540px; height: 100px;
    background: linear-gradient(90deg, var(--tire-dark), var(--tire-mid) 50%, var(--tire-dark));
    border-radius: 10px;
  }
  .box-side__phone {
    position: absolute; left: 110px; top: 500px; display: flex; align-items: center; gap: 10px;
    font-family: "Oswald", sans-serif; font-weight: 600; font-size: 42px; letter-spacing: 2px;
    color: var(--brand-blue);
  }
  .box-side__phone svg { width: 28px; height: 28px; }

  .header-panel {
    position: absolute; left: 40px; top: 630px; width: 420px; height: 230px;
    background: var(--panel-white); box-shadow: 0 2px 10px rgba(0,0,0,.15);
    display: flex; flex-direction: column; align-items: center; justify-content: center; text-align: center;
  }
  .brand-name { font-family: "Oswald", sans-serif; font-weight: 600; color: var(--brand-blue-dark); font-size: 34px; line-height: 1.1; }
  .brand-tagline { font-family: "Oswald", sans-serif; font-weight: 600; color: var(--brand-blue); font-size: 26px; margin-top: 4px; }
  .header-panel__phone { font-family: "Oswald", sans-serif; font-weight: 600; color: var(--brand-blue); font-size: 38px; letter-spacing: 2px; margin-top: 8px; }

  .door-panel {
    position: absolute; left: 490px; top: 630px; width: 670px; height: 230px;
    background: var(--panel-white); box-shadow: 0 2px 10px rgba(0,0,0,.15);
    display: flex; align-items: center; justify-content: space-between; padding: 0 40px;
  }
  .door-panel__note {
    font-family: "Oswald", sans-serif; font-weight: 500; color: var(--brand-blue);
    font-size: 20px; line-height: 1.2; text-transform: uppercase; width: 280px;
  }
  .door-panel__brand { text-align: center; }
</style>
</head>
<body>
  <section class="box-side">
    <svg class="box-side__band" viewBox="0 0 1120 560" aria-hidden="true">
      <path d="M0 0 H1120 V330 C 900 250 620 200 0 190 Z" fill="var(--brand-blue)"/>
    </svg>
    <h1 class="box-side__headline">Don’t wait at a tire shop,<br>wheel come to you!</h1>
    <div class="worker-photo" role="img" aria-label="Photo of a mechanic in red shirt and grey overalls rolling a tire"></div>
    <ul class="service-list">
      <li>Tire mounting &amp; installation</li>
      <li>New &amp; used tires</li>
      <li>Competitive wholesale pricing</li>
      <li>Tire repairs</li>
      <li>Emergency roadside service</li>
      <li>Low profile tires &amp; custom wheels</li>
    </ul>
    <div class="tire-row" role="img" aria-label="Photo of a row of new black tires"></div>
    <div class="box-side__phone">
      <svg viewBox="0 0 24 24" aria-hidden="true"><path fill="var(--brand-blue)" d="M6.6 10.8a15 15 0 0 0 6.6 6.6l2.2-2.2a1 1 0 0 1 1-.25 11.4 11.4 0 0 0 3.6.57 1 1 0 0 1 1 1V20a1 1 0 0 1-1 1A17 17 0 0 1 3 4a1 1 0 0 1 1-1h3.5a1 1 0 0 1 1 1c0 1.25.2 2.45.57 3.6a1 1 0 0 1-.25 1z"/></svg>
      <span>555.014.0392</span>
    </div>
  </section>

  <section class="header-panel">
    <div class="brand-name">Kestrel Roadway Wheels</div>
    <div class="brand-tagline">We Come To You</div>
    <div class="header-panel__phone">555.014.0392</div>
  </section>

  <section class="door-panel">
    <p class="door-panel__note">This truck carries all the equipment needed to get you back on the road!</p>
    <div class="door-panel__brand">
      <div class="brand-name">Kestrel Roadway Wheels</div>
      <div class="brand-tagline">We Come To You</div>
    </div>
  </section>
</body>
</html>
```